New Zealand health product business needs website designed

A website is required for a business that sells New Zealand made products, namely products like infant formula, health products such as NZ honey, supplements, skincare products etc. This is purely an informative website that will introduce the all the different types of products the business has to offer. The target audience will the the Chinese market. The logo is a calligraphy style font in colours 78b643 and 313542 (logo is still being finalised at the moment) so a colour theme to match would be great.

It is crucial that the design communicates the beautiful nature of New Zealand, non-polluted environments, with emphasis on pure, natural and cleaniness.
Updates

A website that I quite like is http://www.frostvalegelato.co.nz

Information is easy to find, layout is nice and clear.                          

Hi all, I have now uploaded a logo for the business "Tawny Crate", please note that this is yet to be finalized however I expect it to be minor changes so please ensure the website theme and colour use go well with the logo. 

There are three scenery images uploaded, designs with any one of them used is fine whichever works better with your design.  Only one image is required on the website, no sliding effects for this.

Also just to clarify my requirements further.  The developer can use HTML, PHP, Javascript, CSS for coding, preferably to have the images cut and a pdf guide provided for things like alignment and sizing etc.

The menu items are Home / Our story / Product outline / Brands / Contact us
Designs are required for all these.  Within the product outline page, the subcategories are -
Infant formulas
Baby supplements
Toddlers products
Honey
Beauty products
Mens supplements
Womens supplements
Health products
Others

   

Target Market(s)

China based customers looking for quality products from New Zealand.

Industry/Entity Type

Health

Requirements
Must have
• clear menu bar in home page, the four main menu items are -
Our story
Product outline
Brands
Contact us
Nice to have
• Space for a large scenery photo in the home page

```html
<!DOCTYPE html>
<html lang="en">
<head>
<meta charset="utf-8">
<title>Tawny Crate</title>
<link rel="stylesheet" href="https://fonts.googleapis.com/css2?family=Arimo:ital,wght@0,400;0,700;1,400&family=Open+Sans:wght@400&family=PT+Sans:wght@400;700&family=PT+Serif:ital@1&display=swap">
<style>
  :root{
    --green-top:#71ab44;
    --green-mid:#5f8f45;
    --green-deep:#3e4c43;
    --nav-light:#4c5063;
    --nav-dark:#2c2f3d;
    --white:#ffffff;
    --ink:#111111;
    --button:#0d8a2e;
    --rule:#cfcfcf;
    --hero-top:#3f6a8f;
    --hero-bottom:#1f3a2a;
    --honey:#f0b43c;
    --pasture:#7fa04e;
    --seed:#c8b690;
  }
  *{margin:0;padding:0;box-sizing:border-box}
  html,body{width:1200px;height:1140px;overflow:hidden}
  body{
    position:relative;
    background:linear-gradient(180deg,var(--green-top) 0,var(--green-top) 8%,var(--green-mid) 50%,var(--green-deep) 100%);
    font-family:"PT Sans",sans-serif;color:var(--white);
  }
  .site-header{position:absolute;left:0;top:0;width:1200px;height:125px;z-index:2}
  .nav-band{position:absolute;left:0;top:56px;width:1200px;height:41px;
    background:linear-gradient(180deg,var(--nav-light),var(--nav-dark));
    box-shadow:0 2px 3px rgba(0,0,0,.35)}
  .logo-tab{position:absolute;left:370px;top:26px;width:460px;height:98px}
  .logo-name{position:absolute;left:0;width:1200px;top:50px;text-align:center;
    font-size:50px;font-weight:400;letter-spacing:3px;color:var(--white);line-height:1}
  .main-nav a{position:absolute;top:68px;font-size:14px;color:var(--white);text-decoration:none;letter-spacing:.3px}
  .nav-sep{position:absolute;top:64px;width:1px;height:24px;background:#6b6e7c}
  .hero{position:absolute;left:100px;top:97px;width:1000px;height:401px;background:var(--white);z-index:1}
  .hero-photo{position:absolute;left:7px;top:0;width:986px;height:395px;
    background:linear-gradient(180deg,var(--hero-top),var(--hero-bottom))}
  .intro{position:absolute;left:130px;top:534px;width:942px;font-family:"Open Sans",sans-serif;font-size:13.5px;letter-spacing:-.15px;line-height:22px}
  .product{position:absolute;top:673px;width:316px;height:183px;border:1px solid #9aa19a;box-shadow:0 1px 4px rgba(0,0,0,.3)}
  .product-photo{height:121px}
  .product-label{height:60px;background:linear-gradient(180deg,#000 0,#0b0b0b 55%,#3a3a3a 100%);position:relative;padding:10px 0 0 33px}
  .product-label svg{position:absolute;left:14px;top:22px}
  .product-title{font-size:25px;line-height:1}
  .product-more{font-family:"PT Serif",serif;font-style:italic;font-size:14px;color:#d8d8d8;line-height:1.1}
  .testimonials{position:absolute;left:113px;top:886px;width:974px;height:145px;background:var(--white);color:var(--ink);font-family:"Arimo",sans-serif}
  .testimonials h2{position:absolute;left:20px;top:24px;width:222px;text-align:center;font-size:20px;line-height:26px;font-weight:700}
  .testimonials .cta{position:absolute;left:35px;top:86px;width:193px;height:31px;background:var(--button);color:var(--white);
    font-size:12px;font-weight:700;text-align:center;line-height:31px;border:2px solid #e2e2e2;outline:1px solid #bbb;text-decoration:none}
  .quote{position:absolute;top:20px;width:318px;font-style:italic;font-size:11.4px;line-height:14.3px}
  .quote-left{left:270px;text-align:left}
  .quote-right{left:640px;width:310px;text-align:justify}
  .quote cite{display:block;margin-top:12px;font-style:normal;font-weight:700;font-size:12px}
  .quote-divider{position:absolute;left:615px;top:14px;width:1px;height:118px;background:var(--rule)}
  .site-footer{position:absolute;left:0;top:1090px;width:1200px;text-align:center;font-family:"Open Sans",sans-serif;font-size:12px}
</style>
</head>
<body>
<header class="site-header">
  <div class="nav-band"></div>
  <svg class="logo-tab" viewBox="0 0 460 98" aria-hidden="true">
    <defs>
      <linearGradient id="tabFill" x1="0" y1="0" x2="0" y2="1">
        <stop offset="0" stop-color="#5a5e72"/><stop offset="1" stop-color="#262836"/>
      </linearGradient>
    </defs>
    <path d="M0 30 C20 30 28 2 50 2 L410 2 C432 2 440 30 460 30 L460 71 L452 71 C438 71 440 96 412 96 L48 96 C20 96 22 71 8 71 L0 71 Z" fill="url(#tabFill)" stroke="#6ea74a" stroke-width="2"/>
  </svg>
  <div class="logo-name">TAWNY CRATE</div>
  <nav class="main-nav">
    <span class="nav-sep" style="left:101px"></span>
    <a href="#" style="left:133px">OUR STORY</a>
    <span class="nav-sep" style="left:228px"></span>
    <a href="#" style="left:248px">PRODUCTS</a>
    <a href="#" style="left:889px">BRANDS</a>
    <span class="nav-sep" style="left:963px"></span>
    <a href="#" style="left:987px">CONTACT US</a>
    <span class="nav-sep" style="left:1098px"></span>
  </nav>
</header>

<section class="hero">
  <div class="hero-photo" role="img" aria-label="Snow-capped mountains behind a forest-lined lake under a blue sky"></div>
</section>

<p class="intro">Orem ipsum dolor sit amet, consectetur adipiscing elit. Mauris vehicula auctor imperdiet. Nulla interdum nisi sit amet turpis congue, placerat fringilla leo varius. In hac habitasse platea dictumst. Integer facilisis metus tortor, ac porta felis interdum at. Sed commodo justo id enim rutrum, ac lobortis diam rhoncus. Donec sed ornare sem. In bibendum augue sed imperdiet adipiscing. Aenean a adipiscing massa. Donec sagittis leo tellus, sit amet vulputate dui luctus et. Sed a lorem ultrices, pellentesque sem quis, interdum quam. Mauris mi arcu, accumsan eget dictum et, tempor vitae mauris. Integer facilisis metus tortor, ac porta felis interdum at. Sed commodo justo id enim rutrum.</p>

<article class="product" style="left:113px">
  <div class="product-photo" role="img" aria-label="Honey dripping from a dipper into a glass bowl" style="background:var(--honey)"></div>
  <div class="product-label">
    <svg width="10" height="16" viewBox="0 0 10 16"><path d="M0 0 L10 8 L0 16 Z" fill="#fff"/></svg>
    <div class="product-title">Natual Honey</div>
    <div class="product-more">Read more about it</div>
  </div>
</article>
<article class="product" style="left:443px">
  <div class="product-photo" role="img" aria-label="Cows grazing on green pasture beside a jug of milk" style="background:var(--pasture)"></div>
  <div class="product-label">
    <svg width="10" height="16" viewBox="0 0 10 16"><path d="M0 0 L10 8 L0 16 Z" fill="#fff"/></svg>
    <div class="product-title">Formula Milk</div>
    <div class="product-more">Read more about it</div>
  </div>
</article>
<article class="product" style="left:771px">
  <div class="product-photo" role="img" aria-label="Wooden spoon of hemp seeds next to a bowl of oil on burlap" style="background:var(--seed)"></div>
  <div class="product-label">
    <svg width="10" height="16" viewBox="0 0 10 16"><path d="M0 0 L10 8 L0 16 Z" fill="#fff"/></svg>
    <div class="product-title">Hemp Seed Oil</div>
    <div class="product-more">Read more about it</div>
  </div>
</article>

<section class="testimonials">
  <h2>Read what our clients have to say:</h2>
  <a class="cta" href="#">READ OUR TESTIMONIALS</a>
  <blockquote class="quote quote-left">“Curabitur ut ipsum quis ipsum tincidunt congue eget non ligula. Nunc odio metus, euismod vitae felis hendrerit, euismod hendrerit nunc. Vestibulum dignissim at leo ut tempor. In vitae tincidunt dolor. Nullam vitae pretium mi, vel elementum sem. ”<cite>- Lan Qiu</cite></blockquote>
  <span class="quote-divider"></span>
  <blockquote class="quote quote-right">“Mauris hendrerit lacus sapien, a sollicitudin purus hendre&shy;rit sed. Nullam vitae enim at libero bibendum interdum. Vivamus quis aliquet velit. Mauris a placerat orci. Donec ut magna urna. Nunc quis augue dolor. Donec quis iaculis massa. Morbi semper egestas rutrum. ”<cite>- Tom Reyes</cite></blockquote>
</section>

<footer class="site-footer">© 2013 Tawny Crate. All rights reserved.</footer>
</body>
</html>
```